Black Car Limousine transportation business in Naples Florida

Always stand for my reliability and RNT stands for Rest, N and T are the first initials of my children's names. It should show professionalism and a dedication to customer service. We keep our clients identities private. Show our professionalism. We are Black car Black tie company. We service transportation on a reserve basis to and from residents, airports, casinos, hotels,

Target Market(s)

It is a Private car service. High end clients. Businesses, Celebrity and athletes. Service to airports, hotels, special events.

Industry/Entity Type

Business

Contact Information for Business Card

A pearl metallic or Luster card. Standard business card size. Would like the name, Company email, show we take credit cards and phone number. Currently I don't have a website but will like to add later.

Logo Text

STEADFAST RNT TRANSPORTATION

Font styles to use
Serif

Colors
eaeaea
000000

Requirements
Must have
• Must have Company email, show we take credit cards and phone number. Currently I don't have a website but will like to add later.
Nice to have
• Would like to stay with a black and white theme. Open to some color trim.
Should not have
• Open to suggestions

```html
<!DOCTYPE html>
<html lang="en">
<head>
<meta charset="utf-8">
<title>Steadfast RNT Transportation Business Card</title>
<link href="https://fonts.googleapis.com/css2?family=Cormorant+Garamond:wght@400;500;600&display=swap" rel="stylesheet">
<style>
  :root {
    --canvas: #ffffff;
    --card-front: #1f1c1d;
    --card-back: #bdbdbf;
    --ink-light: #f2f2f2;
    --ink-dark: #1a1a1a;
    --ink-body: #2b2b2b;
    --ink-muted: #4a4a4a;
    --shadow: rgba(0, 0, 0, 0.28);
  }
  html, body {
    margin: 0;
    padding: 0;
    width: 1200px;
    height: 1011px;
    overflow: hidden;
    background: var(--canvas);
    font-family: "Cormorant Garamond", serif;
  }
  .sheet {
    position: relative;
    width: 1200px;
    height: 1011px;
  }
  .card {
    position: absolute;
    top: 352px;
    width: 520px;
    height: 306px;
    box-shadow: 14px -14px 28px var(--shadow);
    overflow: hidden;
  }
  .card--front {
    left: 60px;
    background: var(--card-front);
  }
  .card--back {
    left: 620px;
    background: var(--card-back);
  }
  .brand {
    position: absolute;
    line-height: 1;
    white-space: nowrap;
  }
  .brand__tagline {
    display: block;
    font-weight: 500;
    font-size: 19px;
    letter-spacing: 0.5px;
    margin-left: 48px;
    margin-bottom: 2px;
  }
  .brand__name {
    display: block;
    font-weight: 500;
    font-size: 62px;
    letter-spacing: 2px;
  }
  .brand__legal {
    display: block;
    font-weight: 600;
    font-size: 11px;
    letter-spacing: 1.6px;
    margin-top: 4px;
  }
  .card--front .brand {
    left: 50%;
    top: 104px;
    transform: translateX(-50%);
    color: var(--ink-light);
  }
  .card--back .brand {
    left: 36px;
    top: 112px;
    color: var(--ink-dark);
  }
  .backdrop {
    position: absolute;
    inset: 0;
    width: 100%;
    height: 100%;
  }
  .contact {
    position: absolute;
    left: 36px;
    top: 218px;
    margin: 0;
    padding: 0;
    list-style: none;
    font-weight: 600;
    font-size: 22px;
    line-height: 25px;
    color: var(--ink-body);
  }
  .payment-note {
    position: absolute;
    right: 40px;
    top: 250px;
    margin: 0;
    font-weight: 500;
    font-size: 14px;
    color: var(--ink-muted);
  }
</style>
</head>
<body>
<main class="sheet">
  <section class="card card--front" aria-label="Card front">
    <div class="brand">
      <span class="brand__tagline">luxury car</span>
      <span class="brand__name">RNT</span>
      <span class="brand__legal">STEADFAST RNT TRANSPORTATION</span>
    </div>
  </section>

  <section class="card card--back" aria-label="Card back">
    <svg class="backdrop" viewBox="0 0 520 306" preserveAspectRatio="none" role="img" aria-label="Soft-focus photograph of a glossy silver luxury car with light reflections">
      <defs>
        <linearGradient id="car-photo" x1="0" y1="0" x2="1" y2="1">
          <stop offset="0" stop-color="#d4d4d6"/>
          <stop offset="0.45" stop-color="#bfbfc1"/>
          <stop offset="1" stop-color="#b3b3b5"/>
        </linearGradient>
        <radialGradient id="car-glint" cx="0.76" cy="0.2" r="0.35">
          <stop offset="0" stop-color="#ffffff" stop-opacity="0.7"/>
          <stop offset="1" stop-color="#ffffff" stop-opacity="0"/>
        </radialGradient>
      </defs>
      <rect width="520" height="306" fill="url(#car-photo)"/>
      <rect width="520" height="306" fill="url(#car-glint)"/>
    </svg>
    <div class="brand">
      <span class="brand__tagline">luxury car</span>
      <span class="brand__name">RNT</span>
      <span class="brand__legal">STEADFAST RNT TRANSPORTATION</span>
    </div>
    <ul class="contact">
      <li>239-55-01-77</li>
      <li>hello@rnt-transport.com</li>
    </ul>
    <p class="payment-note">we take all credit cards</p>
  </section>
</main>
</body>
</html>
```